Exclusive Pet groomer Post Card

We need a design for a direct mailing postcard. We want to include images of some of dogs and cats done the list of our services and the benefits of our company.

I like something like: Does your pet look like any of these or is a similar breed?

If your answer is yes, then it deserves the best groomer in town

any ideas are welcome!

URGENT Mailing Postcard needed!

Elegant, modern and clean sophisticated card that has images of the dogs and cats provided. I will use the original images from the image bank once the project is approved. As a designer you just need to create the layout for this and the organization!

Thanks

Target Market(s)

High Income professionals that will pay for premium services for their pets.

Industry/Entity Type

Pet

Requirements
Must have
• A full color double sided postcard. 5.5 x 8.5 in postcard. (I want to have all pics uploaded. I used some sample images from stock photo but once approved I will purchase the images at the respective site). Must have space to place recipient address and space for NPDS stamp. ( is a postcard to be mailed!)

I would like to have the following text in the post card:

Enhance the beauty of your pets
Pamper your best friend
Give to your dog or cat the stylish treatment it deserves

One of the top groomers in town
Experienced in dogs and cats
Clean individual pet grooming stations (Sanitation and Sterilization)
Services:
Full service grooming* services for dogs and cats include:
Day Spa, High Fashion Haircuts, hair trimming, nail clipping and “Petticures”
Bathing, gentle ear Cleaning, sanitary trim, Brushing, Fluff Drying and Dematting
* Regular grooming ensures happier and healthier pets

Fur Harbor Trim
2716 NE 147th Street, North Miami, Florida 33181
T. 305-647-3918
www.furharbortrim.example
Nice to have
• Logo as in the website

```html
<!DOCTYPE html>
<html lang="en">
<head>
<meta charset="utf-8">
<title>Fur Harbor Trim – Postcard Front</title>
<link rel="stylesheet" href="https://fonts.googleapis.com/css2?family=Cinzel:wght@400;600;700&family=Righteous&display=swap">
<style>
  :root {
    --band: #8a79ae;
    --lavender-deep: #a596c3;
    --lavender-mid: #c5bcd9;
    --lavender-light: #ece8f3;
    --white: #ffffff;
    --magenta: #a93a8c;
    --bullet: #b0449a;
    --fur-brown: #7a5132;
    --fur-tan: #c39a6c;
    --fur-dark: #4a3526;
    --cat-cream: #f1ebe6;
    --cat-shade: #b59c8c;
  }
  * { margin: 0; padding: 0; box-sizing: border-box; }
  html, body { width: 1200px; height: 851px; overflow: hidden; background: var(--white); }
  .postcard { position: relative; width: 1200px; height: 851px; overflow: hidden; }
  .postcard svg { display: block; }
  .title { font-family: "Righteous", "Trebuchet MS", sans-serif; font-size: 56px; fill: var(--white); }
  .pamper { font-family: "Cinzel", Georgia, serif; font-weight: 600; font-size: 33px; fill: var(--magenta); }
  .promise-heading { font-family: "Cinzel", Georgia, serif; font-weight: 700; font-size: 48px; fill: var(--magenta); }
  .promise-item { font-family: "Cinzel", Georgia, serif; font-weight: 600; font-size: 31px; fill: var(--magenta); }
  .promise-note { font-family: "Cinzel", Georgia, serif; font-weight: 600; font-size: 24px; fill: var(--magenta); }
  .bullet { fill: var(--bullet); }
  .brand-name { font-family: "Cinzel", Georgia, serif; font-weight: 700; font-size: 30px; fill: var(--white); }
  .website { font-family: Arial, Helvetica, sans-serif; font-size: 26px; fill: var(--white); }
</style>
</head>
<body>
<div class="postcard">
  <svg width="1200" height="851" viewBox="0 0 1200 851" xmlns="http://www.w3.org/2000/svg">
    <defs>
      <radialGradient id="backdrop" cx="0.45" cy="0.3" r="0.85">
        <stop offset="0" stop-color="var(--lavender-light)"/>
        <stop offset="0.55" stop-color="var(--lavender-mid)"/>
        <stop offset="1" stop-color="var(--lavender-deep)"/>
      </radialGradient>
      <linearGradient id="ribbonTone" x1="0" y1="0" x2="1" y2="0">
        <stop offset="0" stop-color="var(--fur-brown)"/>
        <stop offset="0.6" stop-color="var(--fur-tan)"/>
        <stop offset="1" stop-color="var(--fur-brown)"/>
      </linearGradient>
      <linearGradient id="dogTone" x1="0" y1="0" x2="0" y2="1">
        <stop offset="0" stop-color="var(--fur-dark)"/>
        <stop offset="0.5" stop-color="var(--fur-tan)"/>
        <stop offset="1" stop-color="var(--fur-brown)"/>
      </linearGradient>
      <linearGradient id="catTone" x1="0" y1="0" x2="0" y2="1">
        <stop offset="0" stop-color="var(--cat-shade)"/>
        <stop offset="0.3" stop-color="var(--cat-cream)"/>
        <stop offset="1" stop-color="var(--cat-cream)"/>
      </linearGradient>
      <radialGradient id="furTone" cx="0.5" cy="0.5" r="0.6">
        <stop offset="0" stop-color="#ffffff"/>
        <stop offset="1" stop-color="#eee9e4"/>
      </radialGradient>
      <clipPath id="bowCircleClip"><circle cx="170" cy="198" r="267"/></clipPath>
    </defs>

    <rect width="1200" height="851" fill="url(#backdrop)"/>

    <g class="bow-circle">
      <circle cx="170" cy="198" r="273" fill="var(--white)"/>
      <g clip-path="url(#bowCircleClip)">
        <rect x="-110" y="268" width="560" height="220" fill="url(#ribbonTone)"
              role="img" aria-label="Close-up of a groomed dog's topknot tied with a pink gingham bow"/>
      </g>
    </g>

    <rect class="dog-photo" x="47" y="425" width="463" height="372" rx="150" fill="url(#dogTone)"
          role="img" aria-label="Yorkshire terrier lying down with a pink gingham bow in its hair"/>

    <rect class="cat-photo" x="440" y="137" width="402" height="714" rx="170" fill="url(#catTone)"
          role="img" aria-label="White and chocolate point cat walking and looking upward"/>

    <g class="promise-circle">
      <circle cx="990" cy="440" r="240" fill="var(--white)"/>
      <circle cx="990" cy="440" r="232" fill="url(#furTone)" role="img" aria-label="Soft white fur texture"/>
    </g>

    <rect class="title-band" x="0" y="0" width="1200" height="92" fill="var(--band)"/>
    <text class="title" x="19" y="66" textLength="1154" lengthAdjust="spacingAndGlyphs">ENHANCE THE BEAUTY OF YOUR PETS</text>

    <g class="pamper">
      <text x="24" y="149" textLength="392" lengthAdjust="spacingAndGlyphs">Pamper your best friend</text>
      <text x="19" y="199" textLength="404" lengthAdjust="spacingAndGlyphs">Give to your dog or cat</text>
      <text x="57" y="234" textLength="345" lengthAdjust="spacingAndGlyphs">the stylish treatment</text>
      <text x="132" y="267" textLength="175" lengthAdjust="spacingAndGlyphs">it deserves</text>
    </g>

    <g class="promise">
      <text class="promise-heading" x="863" y="315" textLength="255" lengthAdjust="spacingAndGlyphs">One of the</text>
      <text class="promise-heading" x="814" y="356" textLength="359" lengthAdjust="spacingAndGlyphs">Top Groomers</text>
      <text class="promise-heading" x="896" y="395" textLength="189" lengthAdjust="spacingAndGlyphs">in Town</text>

      <circle class="bullet" cx="866" cy="430" r="7"/>
      <text class="promise-item" x="891" y="441" textLength="249" lengthAdjust="spacingAndGlyphs">Experienced in</text>
      <text class="promise-item" x="891" y="470" textLength="244" lengthAdjust="spacingAndGlyphs">dogs and cats</text>

      <circle class="bullet" cx="866" cy="505" r="7"/>
      <text class="promise-item" x="891" y="516" textLength="291" lengthAdjust="spacingAndGlyphs">Clean individual</text>
      <text class="promise-item" x="891" y="549" textLength="237" lengthAdjust="spacingAndGlyphs">pet grooming</text>
      <text class="promise-item" x="891" y="582" textLength="142" lengthAdjust="spacingAndGlyphs">stations</text>
      <text class="promise-note" x="889" y="610" textLength="220" lengthAdjust="spacingAndGlyphs">(Sanitation and</text>
      <text class="promise-note" x="889" y="638" textLength="189" lengthAdjust="spacingAndGlyphs">Sterilization)</text>
    </g>

    <g class="brand">
      <circle cx="892" cy="752" r="10" fill="var(--white)"/>
      <text class="brand-name" x="914" y="763" textLength="258" lengthAdjust="spacingAndGlyphs">Fur Harbor Trim</text>
    </g>
    <text class="website" x="875" y="825" textLength="303" lengthAdjust="spacingAndGlyphs">www.furharbortrim.example</text>
  </svg>
</div>
</body>
</html>
```